Simple elegant feminine design - Going out on my own as a Mortgage Broker.
My thoughts are the following details on the Front, middle of the card possibly? Phone and email smaller font than my name?
Marnie Veltrin
Finance Specialist
p: 0438 215 962
e: marnie@veltrinlending.com.au
Bottom of the card
residential / commercial / equipment
I would like the Font in Rose Gold maybe white or black background? or Possibly a stone grey - are you able to do a few options? I'd like them embossed
Then I had an idea as a simple logo as per the attached if you get the idea in my scribble, my initials, capital M attached to a small v that leads/follows into a circle? Thicker Font In Rose Gold, middle of the card at the back.
Very open to ideas though and what colour you think would look better with the Rose Gold.
Thanks so much for your help, I am not very creative and savvy with this stuff :-)
Industry/Entity Type
Finance
Contact Information for Business Card
Marnie Veltrin
p: 0438 215 962
Look and feel

```html
<!DOCTYPE html>
<html lang="en">
<head>
<meta charset="utf-8">
<title>Marnie's Business Cards</title>
<link rel="stylesheet" href="https://fonts.googleapis.com/css2?family=Exo+2:ital,wght@1,800&family=Lato:wght@300&family=Open+Sans:wght@400&display=swap">
<style>
  :root {
    --backdrop: #eeeeef;
    --card: #939396;
    --ink-light: #ffffff;
    --ink-dark: #1e1e20;
    --mark: #2b2b2d;
  }
  html, body {
    margin: 0;
    padding: 0;
    width: 1200px;
    height: 1200px;
    overflow: hidden;
    background: var(--backdrop);
  }
  .canvas {
    position: relative;
    width: 1200px;
    height: 1200px;
  }
  .card {
    position: absolute;
    left: 156px;
    width: 888px;
    height: 522px;
    background: var(--card);
  }
  .card--front { top: 44px; }
  .card--back { top: 634px; }

  .identity {
    position: absolute;
    top: 98px;
    left: 0;
    width: 100%;
    text-align: center;
    color: var(--ink-light);
  }
  .identity__name {
    margin: 0;
    font-family: "Exo 2", sans-serif;
    font-weight: 800;
    font-style: italic;
    font-size: 36px;
    line-height: 48px;
    letter-spacing: 0.5px;
  }
  .identity__title {
    display: inline-flex;
    align-items: center;
    gap: 4px;
    margin-top: 0;
    font-family: "Lato", sans-serif;
    font-weight: 300;
    font-size: 22px;
    line-height: 28px;
  }
  .identity__title::before,
  .identity__title::after {
    content: "";
    display: block;
    width: 42px;
    height: 1px;
    background: var(--ink-light);
  }

  .contact {
    position: absolute;
    top: 274px;
    left: 0;
    width: 100%;
    text-align: center;
    font-family: "Open Sans", sans-serif;
    font-size: 22px;
    color: var(--ink-light);
  }
  .contact__line {
    margin: 0 0 14px;
    line-height: 28px;
  }
  .contact__label { color: var(--ink-dark); }

  .services {
    position: absolute;
    top: 470px;
    left: 123px;
    display: flex;
    align-items: center;
    font-family: "Open Sans", sans-serif;
    font-size: 22px;
    letter-spacing: 5px;
    color: var(--ink-light);
    line-height: 30px;
  }
  .services__divider {
    color: var(--ink-dark);
    margin: 0 34px 0 36px;
    letter-spacing: 0;
  }

  .brand {
    position: absolute;
    top: 0;
    left: 0;
    width: 100%;
    height: 100%;
    display: flex;
    align-items: center;
    justify-content: center;
    gap: 14px;
  }
  .brand__dot {
    width: 26px;
    height: 26px;
    border-radius: 50%;
    background: var(--mark);
  }
  .brand__name {
    font-family: "Open Sans", sans-serif;
    font-size: 30px;
    color: var(--mark);
    letter-spacing: 1px;
  }
</style>
</head>
<body>
  <main class="canvas">
    <section class="card card--front">
      <header class="identity">
        <h1 class="identity__name">Marnie Veltrin</h1>
        <div class="identity__title">Finance Specialist</div>
      </header>
      <div class="contact">
        <p class="contact__line"><span class="contact__label">P</span> : 0438 215 962</p>
        <p class="contact__line"><span class="contact__label">E</span> : marnie@veltrinlending.com.au</p>
      </div>
      <div class="services">
        <span>residential</span>
        <span class="services__divider">|</span>
        <span>commercial</span>
        <span class="services__divider">|</span>
        <span>equipment</span>
      </div>
    </section>

    <section class="card card--back">
      <div class="brand">
        <span class="brand__dot"></span>
        <span class="brand__name">Veltrin Lending</span>
      </div>
    </section>
  </main>
</body>
</html>
```